Harbor Sprig small batch hot sauce label project

I am launching a line of small batch sauces (hot sauces, bbq sauces) and I need a label for my bottles. I have a logo that I like, I'm not completely married to it but It is a good logo. I would like the name of my business and the name of the sauce on the label. Something fun, edgy that would make you want to pick it up off the shelf.

Target Market(s)

Milennials, food bloggers, stay at home moms who want to amp up their dishes with a really good sauce

Industry/Entity Type

Cooking

Requirements
Must have
• I am open to interpretation
Nice to have
• Maybe a bomb cloud since I want to go in the sauce bomb direction.

```html
<!DOCTYPE html>
<html lang="en">
<head>
<meta charset="utf-8">
<title>Harbor Sprig Sauce Labels</title>
<link href="https://fonts.googleapis.com/css2?family=Bowlby+One&family=Bangers&family=Bungee&display=swap" rel="stylesheet">
<style>
  :root {
    --page: #ffffff;
    --bbq-base: #f7a90f;
    --bbq-light: #fcc52c;
    --hot-base: #9c1b1d;
    --hot-light: #b5282a;
    --ink: #111111;
    --band: #1e1e1e;
    --sauce-red: #e3100f;
    --sauce-gold: #e0b10c;
    --brand-orange: #d8501a;
    --brand-cream: #f1e2dc;
    --cloud-pink: #f6c6c6;
    --cloud-white: #f4f4f4;
  }
  html, body {
    margin: 0;
    padding: 0;
    width: 1198px;
    height: 1200px;
    overflow: hidden;
    background: var(--page);
  }
  .canvas {
    position: relative;
    width: 1198px;
    height: 1200px;
  }
  .neck-label, .main-label {
    position: absolute;
    box-sizing: border-box;
    display: flex;
    flex-direction: column;
    align-items: center;
  }
  .neck-label {
    width: 256px;
    height: 128px;
    justify-content: center;
    top: 120px;
  }
  .main-label {
    width: 332px;
    height: 606px;
    top: 320px;
    padding-top: 20px;
  }
  .label--bbq.neck-label { left: 212px; }
  .label--bbq.main-label { left: 174px; }
  .label--hot.neck-label { left: 700px; }
  .label--hot.main-label { left: 662px; }

  .label--bbq { background: linear-gradient(135deg, var(--bbq-base), var(--bbq-light) 50%, var(--bbq-base)); }
  .label--hot { background: linear-gradient(135deg, var(--hot-base), var(--hot-light) 50%, var(--hot-base)); }

  .brand {
    display: flex;
    align-items: center;
    gap: 8px;
    font-family: "Bungee", sans-serif;
    letter-spacing: 1px;
  }
  .brand-mark {
    width: 14px;
    height: 14px;
  }
  .neck-label .brand { font-size: 19px; }
  .main-label .brand { font-size: 13px; margin-top: 18px; }
  .label--bbq .brand { color: var(--brand-orange); }
  .label--bbq .brand-mark { background: var(--ink); }
  .label--hot .brand { color: var(--brand-cream); }
  .label--hot .brand-mark { background: var(--brand-cream); }

  .sauce-name {
    font-family: "Bowlby One", sans-serif;
    font-size: 96px;
    line-height: 1;
    margin: 0;
    letter-spacing: 2px;
  }
  .label--bbq .sauce-name { color: var(--ink); }
  .label--hot .sauce-name { color: #ffffff; font-size: 92px; }

  .sauce-band {
    width: 224px;
    height: 56px;
    margin-top: 6px;
    background: var(--band);
    display: flex;
    align-items: center;
    justify-content: center;
    font-family: "Bangers", sans-serif;
    font-size: 50px;
    letter-spacing: 2px;
  }
  .label--bbq .sauce-band { color: var(--sauce-red); }
  .label--hot .sauce-band { color: var(--sauce-gold); }

  .blast-art {
    width: 220px;
    height: 340px;
    margin-top: 16px;
    border-radius: 110px 110px 40px 40px;
  }
  .label--bbq .blast-art { background: radial-gradient(circle at 50% 30%, var(--cloud-pink), #c98f8a 70%, #3a2a28); }
  .label--hot .blast-art { background: radial-gradient(circle at 50% 30%, var(--cloud-white), #bdbdbd 70%, #2a2a2a); }
</style>
</head>
<body>
  <main class="canvas">
    <section class="neck-label label--bbq" aria-label="BBQ sauce neck label">
      <div class="brand"><span class="brand-mark"></span>Harbor Sprig</div>
    </section>
    <section class="main-label label--bbq" aria-label="BBQ sauce front label">
      <h1 class="sauce-name">BBQ</h1>
      <div class="sauce-band">SAUCE</div>
      <div class="blast-art" role="img" aria-label="Pink mushroom cloud explosion illustration"></div>
      <div class="brand"><span class="brand-mark"></span>Harbor Sprig</div>
    </section>

    <section class="neck-label label--hot" aria-label="Hot sauce neck label">
      <div class="brand"><span class="brand-mark"></span>Harbor Sprig</div>
    </section>
    <section class="main-label label--hot" aria-label="Hot sauce front label">
      <h1 class="sauce-name">HOT</h1>
      <div class="sauce-band">SAUCE</div>
      <div class="blast-art" role="img" aria-label="White mushroom cloud explosion illustration"></div>
      <div class="brand"><span class="brand-mark"></span>Harbor Sprig</div>
    </section>
  </main>
</body>
</html>
```